R&t subterra

We specialize in CIPP pipe lining but do other underground utilities trenchless as well.

Target Market(s)

Trenchless sewer replacement

Contact Information for Business Card

Doug Falvey 715-482-6170 Wisconsin rapids, wi

```html
<!DOCTYPE html>
<html lang="en">
<head>
<meta charset="utf-8">
<title>R&amp;t subterra — Business Cards</title>
<link href="https://fonts.googleapis.com/css2?family=Poppins:wght@500;600;700&display=swap" rel="stylesheet">
<style>
  :root {
    --brand-blue: #2f8ecd;
    --arc-grey: #a9a9a9;
    --icon-grey: #9c9c9c;
    --tagline-grey: #8a8a8a;
    --card-white: #ffffff;
    --backdrop: #e4e4e4;
  }
  html, body {
    margin: 0;
    width: 1200px;
    height: 1200px;
    overflow: hidden;
    background: var(--backdrop);
  }
  .card {
    position: absolute;
    left: 174px;
    width: 853px;
    height: 474px;
    box-shadow: 0 14px 26px rgba(0,0,0,0.28);
  }
  .card--front { top: 60px; }
  .card--back { top: 629px; }
  .card svg { display: block; width: 100%; height: 100%; }

  .side-panel { fill: var(--brand-blue); }
  .arc-gap { fill: var(--card-white); }
  .arc-grey { fill: var(--arc-grey); }
  .contact-band { fill: var(--brand-blue); }

  .brand-dot { fill: var(--arc-grey); }
  .brand-name {
    font-family: 'Poppins', sans-serif;
    font-weight: 700;
    font-size: 42px;
    fill: var(--brand-blue);
  }
  .contact-person {
    font-family: 'Poppins', sans-serif;
    font-weight: 500;
    font-size: 16px;
    letter-spacing: 2px;
    fill: var(--tagline-grey);
  }
  .phone-number {
    font-family: 'Poppins', sans-serif;
    font-weight: 600;
    font-size: 27px;
  }
  .web-address, .street-address {
    font-family: 'Poppins', sans-serif;
    font-weight: 600;
    font-size: 13px;
  }

  .contact--light .contact-text { fill: var(--brand-blue); }
  .contact--light .icon-fill { fill: var(--icon-grey); }
  .contact--light .icon-stroke { stroke: var(--icon-grey); }
  .contact--light .icon-cutout { fill: var(--card-white); }

  .contact--dark .contact-text { fill: var(--card-white); }
  .contact--dark .icon-fill { fill: var(--card-white); }
  .contact--dark .icon-stroke { stroke: var(--card-white); }
  .contact--dark .icon-cutout { fill: var(--brand-blue); }
</style>
</head>
<body>

<section class="card card--front">
  <svg viewBox="0 0 682 379" xmlns="http://www.w3.org/2000/svg">
    <rect class="side-panel" width="682" height="379"/>
    <ellipse class="arc-gap" cx="500" cy="190" rx="412" ry="336"/>
    <ellipse class="arc-grey" cx="500" cy="190" rx="404" ry="328"/>
    <ellipse class="arc-gap" cx="520" cy="190" rx="412" ry="288"/>

    <g class="brand">
      <circle class="brand-dot" cx="300" cy="112" r="34"/>
      <text class="brand-name" x="348" y="128">R&amp;t subterra</text>
      <text class="contact-person" x="388" y="166">DOUG FALVEY</text>
    </g>

    <g class="contact contact--light">
      <circle class="icon-fill" cx="307" cy="244" r="11"/>
      <path class="icon-cutout" d="M302 238 q-2 7 5 13 l3 -3 l-3 -3 l-2 2 q-3 -3 -3 -6 l2 -1 l-2 -4 z"/>
      <text class="contact-text phone-number" x="343" y="254">715 - 482 - 6170</text>

      <circle class="icon-stroke" cx="307" cy="280" r="9" fill="none" stroke-width="2"/>
      <path class="icon-stroke" d="M298 280 h18 M307 271 v18 M300 274 h14 M300 286 h14" fill="none" stroke-width="1.4"/>
      <path class="icon-fill" d="M309 282 l9 4 l-4 1 l3 4 l-2 1 l-3 -4 l-2 3 z"/>
      <text class="contact-text web-address" x="345" y="285">www.rtsubterra.com</text>

      <path class="icon-fill" d="M307 328 c-5 -7 -9 -11 -9 -16 a9 9 0 0 1 18 0 c0 5 -4 9 -9 16 z"/>
      <circle class="icon-cutout" cx="307" cy="312" r="3.5"/>
      <text class="contact-text street-address" x="345" y="322">Wisconsin Rapids, WI</text>
    </g>
  </svg>
</section>

<section class="card card--back">
  <svg viewBox="0 0 682 379" xmlns="http://www.w3.org/2000/svg">
    <defs>
      <clipPath id="band-clip">
        <ellipse cx="524" cy="190" rx="404" ry="280"/>
      </clipPath>
    </defs>
    <rect class="side-panel" width="682" height="379"/>
    <ellipse class="arc-gap" cx="500" cy="190" rx="412" ry="336"/>
    <ellipse class="arc-grey" cx="500" cy="190" rx="404" ry="328"/>
    <ellipse class="arc-gap" cx="520" cy="190" rx="412" ry="288"/>
    <rect class="contact-band" x="90" y="212" width="592" height="133" clip-path="url(#band-clip)"/>

    <g class="brand">
      <circle class="brand-dot" cx="300" cy="112" r="34"/>
      <text class="brand-name" x="348" y="128">R&amp;t subterra</text>
      <text class="contact-person" x="388" y="166">DOUG FALVEY</text>
    </g>

    <g class="contact contact--dark">
      <circle class="icon-fill" cx="307" cy="244" r="11"/>
      <path class="icon-cutout" d="M302 238 q-2 7 5 13 l3 -3 l-3 -3 l-2 2 q-3 -3 -3 -6 l2 -1 l-2 -4 z"/>
      <text class="contact-text phone-number" x="343" y="254">715 - 482 - 6170</text>

      <circle class="icon-stroke" cx="307" cy="280" r="9" fill="none" stroke-width="2"/>
      <path class="icon-stroke" d="M298 280 h18 M307 271 v18 M300 274 h14 M300 286 h14" fill="none" stroke-width="1.4"/>
      <path class="icon-fill" d="M309 282 l9 4 l-4 1 l3 4 l-2 1 l-3 -4 l-2 3 z"/>
      <text class="contact-text web-address" x="345" y="285">www.rtsubterra.com</text>

      <path class="icon-fill" d="M307 328 c-5 -7 -9 -11 -9 -16 a9 9 0 0 1 18 0 c0 5 -4 9 -9 16 z"/>
      <circle class="icon-cutout" cx="307" cy="312" r="3.5"/>
      <text class="contact-text street-address" x="345" y="322">Wisconsin Rapids, WI</text>
    </g>
  </svg>
</section>

</body>
</html>
```